Shipping and Logistics, Project

Project description : Company Profile

A total logistics company covering domestic / international freight forwarding, warehouse management services, haulage, supply chain management, transport management & distribution, procurement & assembly services, shipping, chartering & bunker services, project logistics & tax exemption consultancy, oil & gas logistics, halal logistics services & integrated logistics management. We’re a well-established and experienced freight forwarder in Kuala Lumpur, Malaysia. We specialize in customized value-added solution that optimizes your supply chain by trimming inventory, reducing logistics cost and enhancing your customer service levels.

As a member of the Continental Parcel and Carriage Alliance which comprise of 170 global freight agents in 80 countries that promotes great handling in cross-trade logistics and freighting. You could rely on our efficiency in handlings of export cargo (FCL, LCL, Bulk and Conventional) between our global network offices worldwide with a total scale of 10,000 groomed specialists in various logistics division working together to ensure delivery task meets with your expectation. With our dedicated qualified and experienced professionals, we are fully committed to serving our clients.

Our generic services are listed below for your reference:

• Air Freight
• Ocean Freight FCL & LCL
• Container Haulage
• Warehousing
• Transportation and Distribution within Malaysia and Thailand
• Cross-Border Road Line-hauls between Thailand, Malaysia, Singapore and Laos
• Customs Brokerage and Forwarding
• Project Cargo Freight Forwarding for setting up of new plants / factories and ad hoc heavy-lift
• Air-Sea-Road-Rail multi-modal options
• Import / Export / Storage / Documentation / Handling of DG / Hazmat
• Vessel and Aircraft Charters

Our Mission
Based on the motto “Quick, Reliable and Polite”, we are dedicated to upholding the following three points corporate philosophy:
1. Adhering to the principle that “the customer always comes first”.
2. Contributing to the development of the local community.
3. Making it our duty to be responsible and sincere.

Our Edge
• One-Stop Logistics Solutions
• Extensive Network Throughout Malaysia
• Highly Qualified and Experienced Pool of Professionals
• Comprehensive IT Solutions
• Innovative and Customer-focused Solutions
• Flexible and Consistent in Managing Exceptions
• Total Supply Chain Visibility

Target Market
1. We sell the logistics services to all the industry in Malaysia and Worldwide. (ONE Stop Logistics Solutions)

Competitor
1. RT Vollmark
2. Corventa Transport
3. Brastow + Feld
4. TOLRI
5. QVN
6. Trundelles
7. Wiro Logistics

Rules for Picking a Company Name
1. Unique and unforgettable
2. Avoid unusual spellings
3. Easy to pronounce and remember
4. Keep it simple
5. Make some sense
6. Give a clue

Rules for Picking a Company Logo
4. Keep it simple
5. Make some sense
6. Give a clue

1. Simplicity
2. Memorability
3. Originality
4. Modern Yet Timeless
5. Balance
6. Complementary
7. Versatility

Stationery Information
1. Company Name : Tenhaul Solutions Sdn Bhd
2. Company Registration : 2738516-P
3. Address : 42-07, Jalan Seri Dedap 5, Taman Bukit Kenari, 81100 Johor Bahru, Johor, Malaysia.
4. Name : Derek Tan
5. Position : Manager
6. Mobile No : (+6019) 4183907
7. Office No : (+607) 2918476
8. Fax No : Not Available
9. Email Address : derek.tan@tenhaul-solutions.example
10. Web Domain : www.tenhaul-solutions.example
11. Company Slogan : Be Globally Connected

Target Market(s)

Corporate Company

Industry/Entity Type

Shipping and Logistics Industry

Requirements
Must have
• Company Full Name : TENHAUL SOLUTIONS SDN. BHD.
Nice to have
• Keep it simple and unforgettable ...

```html
<!DOCTYPE html>
<html lang="en">
<head>
<meta charset="utf-8">
<title>Tenhaul Solutions – Stationery</title>
<link href="https://fonts.googleapis.com/css2?family=Lato:wght@400;700&display=swap" rel="stylesheet">
<style>
  :root{
    --backdrop:#b5b5b5;
    --paper:#ffffff;
    --ink:#1f1f1f;
    --dark:#2a2a2a;
    --blue:#3a86cc;
    --faint:#e3edf7;
    --body-text:#222222;
  }
  *{box-sizing:border-box;margin:0;padding:0}
  html,body{width:1200px;height:1200px;overflow:hidden}
  body{background:var(--backdrop);font-family:'Lato',sans-serif;color:var(--ink);position:relative}
  .piece{position:absolute;background:var(--paper);overflow:hidden}
  .piece.dark{background:var(--dark);color:#fff}
  .card{width:304px;height:174px}

  /* brand lockup */
  .brand{position:absolute;display:flex;align-items:center;gap:.4em;font-weight:700;color:var(--blue);white-space:nowrap;letter-spacing:.02em}
  .brand-square{width:1.1em;height:1.1em;background:var(--blue);flex:none}
  .brand-name{line-height:1}
  .brand.center{left:50%;top:50%;transform:translate(-50%,-50%)}

  .faint-mark{position:absolute;background:var(--faint)}
  .dark .faint-mark{background:var(--blue)}

  .person{position:absolute}
  .person .name{font-size:11px;line-height:1.2}
  .person .role{font-size:8px;margin-top:2px}

  .contacts{position:absolute;font-size:9px;line-height:13.5px;white-space:nowrap}
  .contacts .gap{height:6px}
  .contacts b{font-weight:400;color:var(--blue)}
  .divider{position:absolute;width:1px;background:var(--blue)}

  /* letterhead */
  .letter{width:407px;height:575px;font-size:7.7px;line-height:14.3px;color:var(--body-text)}
  .letter .addressee{position:absolute;left:28px;top:82px;font-weight:700}
  .letter .body{position:absolute;left:28px;top:152px;width:354px;color:var(--body-text)}
  .letter .body p{margin-bottom:14.3px}
  .letter .closing{position:absolute;left:28px;top:386px}
  .letter .signature{position:absolute;left:28px;top:400px;width:88px;height:40px;background:linear-gradient(90deg,#dcdcdc,#f2f2f2)}
  .letter .sign-name{position:absolute;left:28px;top:443px}
  .letter .small-contacts{font-size:5px;line-height:7.6px}
  .letter .small-person{position:absolute;left:253px;top:38px;font-size:5.5px;line-height:7px}
  .letter .small-person .role{font-size:4px}
  .slogan{position:absolute;left:0;right:0;top:526px;text-align:center;color:var(--blue);font-size:8.5px;letter-spacing:.02em;line-height:12px}
  .slogan-line{position:absolute;top:532px;height:1px;background:var(--blue);width:100px}
  .footer-info{position:absolute;left:0;right:0;top:544px;text-align:center;font-size:5px;line-height:8.5px}

  .envelope{width:503px;height:227px}
  .env-address{position:absolute;left:23px;top:56px;font-size:5.5px;line-height:8px}
</style>
</head>
<body>

<!-- Row 1 -->
<section class="piece card" style="left:119px;top:112px">
  <div class="person" style="left:18px;top:17px"><div class="name">Derek Tan</div><div class="role">Manager</div></div>
  <div class="faint-mark" style="left:200px;top:50px;width:100px;height:100px"></div>
  <div class="contacts" style="left:18px;top:99px">
    <div><b>M:</b> (+6019) 4183907</div><div><b>P:</b> (+607) 2918476</div><div class="gap"></div>
    <div><b>E:</b> derek.tan@tenhaul-solutions.example</div><div><b>W:</b> www.tenhaul-solutions.example</div>
  </div>
</section>

<section class="piece card dark" style="left:451px;top:112px">
  <div class="brand center" style="font-size:21px"><span class="brand-square"></span><span class="brand-name">TENHAUL SOLUTIONS</span></div>
</section>

<section class="piece card" style="left:784px;top:112px">
  <div class="brand" style="left:18px;top:83px;font-size:7px"><span class="brand-square"></span><span class="brand-name">TENHAUL SOLUTIONS</span></div>
  <div class="divider" style="left:120px;top:38px;height:98px"></div>
  <div class="person" style="left:132px;top:39px"><div class="name">Derek Tan</div><div class="role">Manager</div></div>
  <div class="contacts" style="left:132px;top:77px;font-size:8.6px">
    <div><b>M:</b> (+6019) 4183907</div><div><b>P:</b> (+607) 2918476</div><div class="gap"></div>
    <div><b>E:</b> derek.tan@tenhaul-solutions.example</div><div><b>W:</b> www.tenhaul-solutions.example</div>
  </div>
  <svg style="position:absolute;left:0;top:159px" width="304" height="15" viewBox="0 0 304 15" aria-hidden="true">
    <polygon points="0,0 83,0 76,15 0,15" fill="var(--dark)"/>
    <polygon points="89,0 304,0 304,15 82,15" fill="var(--blue)"/>
  </svg>
</section>

<!-- Row 2 -->
<section class="piece card" style="left:119px;top:303px">
  <div class="person" style="left:19px;top:17px"><div class="name">Derek Tan</div><div class="role">Manager</div></div>
  <div class="brand" style="left:20px;top:121px;font-size:6.5px"><span class="brand-square"></span><span class="brand-name">TENHAUL SOLUTIONS</span></div>
  <div class="divider" style="left:122px;top:93px;height:63px"></div>
  <div class="contacts" style="left:128px;top:93px">
    <div><b>M:</b> (+6019) 4183907</div><div><b>P:</b> (+607) 2918476</div><div class="gap"></div>
    <div><b>E:</b> derek.tan@tenhaul-solutions.example</div><div><b>W:</b> www.tenhaul-solutions.example</div>
  </div>
</section>

<section class="piece card dark" style="left:451px;top:303px">
  <div class="person" style="left:19px;top:17px"><div class="name">Derek Tan</div><div class="role">Manager</div></div>
  <div class="faint-mark" style="left:6px;top:112px;width:66px;height:66px"></div>
  <div class="contacts" style="left:127px;top:98px">
    <div><b>M:</b> (+6019) 4183907</div><div><b>P:</b> (+607) 2918476</div><div class="gap"></div>
    <div><b>E:</b> derek.tan@tenhaul-solutions.example</div><div><b>W:</b> www.tenhaul-solutions.example</div>
  </div>
</section>

<section class="piece card" style="left:784px;top:303px">
  <div class="brand center" style="font-size:21px"><span class="brand-square"></span><span class="brand-name">TENHAUL SOLUTIONS</span></div>
</section>

<!-- Letterhead -->
<section class="piece letter" style="left:119px;top:520px">
  <div class="brand" style="left:28px;top:34px;font-size:13px"><span class="brand-square"></span><span class="brand-name">TENHAUL SOLUTIONS</span></div>
  <div class="small-person"><div><b>Derek Tan</b></div><div class="role">Manager</div></div>
  <div class="divider" style="left:288px;top:28px;height:40px"></div>
  <div class="contacts small-contacts" style="left:292px;top:29px">
    <div><b>M:</b> (+6019) 4183907</div><div><b>P:</b> (+607) 2918476</div>
    <div><b>E:</b> derek.tan@tenhaul-solutions.example</div><div><b>W:</b> www.tenhaul-solutions.example</div>
  </div>
  <div class="faint-mark" style="left:258px;top:436px;width:140px;height:140px"></div>
  <div class="addressee">To<br>Lorem Ipsum is simply<br>Lorem Ipsum is Lorem Ipsum is<br>Lorem Ipsum is</div>
  <div class="body">
    <p>dummy text of the printing and typesetting industry. Lorem Ipsum has been the industry's standard dummy text ever since the 1500s, when an unknown printer took a galley of type and scrambled it to make a type specimen book. It has survived not only five centuries, but also the leap into electronic typesetting, remaining essentially unchanged.</p>
    <p>It is a long established fact that a reader will be distracted by the readable content of a page when looking at its layout. The point of using Lorem Ipsum is that it has a more-or-less normal distribution of letters, as opposed to using 'Content here, content here', making it look like readable English. Many desktop publishing packages and web page editors now use Lorem Ipsum as their default model text, and a search for 'lorem .</p>
    <p>Contrary to popular belief, Lorem Ipsum is not simply random text. It has roots in a piece of classical Latin literature from 45 BC, making it over 2000 years old. Harold Penwright, a Latin professor at Ashmoor College in Vermont, looked up one of the more obscure Latin words, consectetur, from a Lorem Ipsum passage,</p>
  </div>
  <div class="closing">Lorem Ipsum</div>
  <div class="signature" role="img" aria-label="Handwritten signature"></div>
  <div class="sign-name">Lorem Ipsum is a dummy</div>
  <div class="slogan-line" style="left:28px"></div>
  <div class="slogan">BE GLOBALLY CONNECTED</div>
  <div class="slogan-line" style="right:28px"></div>
  <div class="footer-info">Tenhaul Solutions Sdn Bhd &nbsp;&nbsp;|&nbsp;&nbsp; Registration#: 2738516-P<br>Address : 42-07, Jalan Seri Dedap 5, Taman Bukit Kenari, 81100 Johor Bahru, Johor, Malaysia.</div>
</section>

<!-- Envelope front -->
<section class="piece envelope" style="left:584px;top:557px">
  <div class="brand" style="left:23px;top:24px;font-size:10px"><span class="brand-square"></span><span class="brand-name">TENHAUL SOLUTIONS</span></div>
  <div class="env-address">42-07, Jalan Seri Dedap 5,<br>Taman Bukit Kenari, 81100 Johor<br>Bahru, Johor, Malaysia.</div>
  <div class="faint-mark" style="left:380px;top:96px;width:112px;height:112px"></div>
</section>

<!-- Envelope back -->
<section class="piece envelope" style="left:584px;top:811px">
  <svg style="position:absolute;left:0;top:0" width="503" height="60" viewBox="0 0 503 60" aria-hidden="true">
    <path d="M0,0 H503 V25 L270,55 Q251,58 232,55 L0,25 Z" fill="var(--dark)"/>
  </svg>
  <div class="brand" style="left:50%;top:14px;transform:translateX(-50%);font-size:9px"><span class="brand-square"></span><span class="brand-name">TENHAUL</span></div>
</section>

</body>
</html>
```